Modern Business Card for Industrial Company

We need business cards updated with modern fonts and make it look more technical, sharp and clean. The logo should not be changed, but we are looking for fresh solutions for how other information on the card is laid out in an interesting way. The company provides machinery and services to the ceramic industry and deals with cutting-edge technology. The design should reflect a technologically advanced and modern company that deals with the latest European technologies.

Font styles to use
Sans Serif

Requirements
Must have
• Modern fonts, technical look and feel

```html
<!DOCTYPE html>
<html lang="en">
<head>
<meta charset="utf-8">
<title>KR Tecnica — Business Card</title>
<link href="https://fonts.googleapis.com/css2?family=Montserrat:wght@400;500;700&display=swap" rel="stylesheet">
<style>
  :root {
    --backdrop: #0a4690;
    --card: #fbfbfb;
    --brand-blue: #0b4f8f;
    --accent-red: #b3141c;
    --text-grey: #9b9fa4;
  }
  * { margin: 0; padding: 0; box-sizing: border-box; }
  html, body {
    width: 1189px;
    height: 1200px;
    overflow: hidden;
    background: var(--backdrop);
    font-family: "Montserrat", sans-serif;
  }
  .sheet { position: relative; width: 1189px; height: 1200px; }
  .card {
    position: absolute;
    left: 261px;
    width: 667px;
    height: 381px;
    background: var(--card);
    border-radius: 22px;
  }
  .card--front { top: 171px; }
  .card--back { top: 648px; }

  .wordmark {
    position: absolute;
    display: flex;
    align-items: center;
    gap: 8px;
    font-weight: 700;
    font-size: 29px;
    color: var(--brand-blue);
    letter-spacing: 0.01em;
    white-space: nowrap;
  }
  .wordmark__square {
    width: 14px;
    height: 14px;
    background: var(--brand-blue);
  }
  .card--front .wordmark { left: 93px; top: 172px; }
  .card--back .wordmark { left: 50%; top: 50%; transform: translate(-50%, -50%); }

  .holder { position: absolute; left: 357px; top: 88px; }
  .holder__name {
    font-weight: 700;
    font-size: 31px;
    color: var(--brand-blue);
    line-height: 1.1;
  }
  .holder__title {
    margin-top: 4px;
    font-weight: 500;
    font-size: 18px;
    color: var(--accent-red);
  }
  .contact { list-style: none; margin-top: 16px; }
  .contact__item {
    display: flex;
    align-items: center;
    gap: 13px;
    font-size: 16px;
    color: var(--text-grey);
    line-height: 1.2;
    margin-bottom: 8px;
  }
  .contact__icon { width: 12px; height: 12px; flex: none; fill: var(--accent-red); }
  .contact__icon--stroke { fill: none; stroke: var(--accent-red); stroke-width: 1.6; }
</style>
</head>
<body>
<main class="sheet">
  <section class="card card--front">
    <div class="wordmark"><span class="wordmark__square"></span>KR Tecnica</div>
    <div class="holder">
      <h1 class="holder__name">Marco Ferrand</h1>
      <p class="holder__title">President</p>
      <ul class="contact">
        <li class="contact__item">
          <svg class="contact__icon" viewBox="0 0 12 12" aria-hidden="true"><path d="M2.3 0.8l2 2-1 1.4c0.7 1.5 1.8 2.6 3.3 3.3l1.4-1 2 2-1.3 1.6C5.4 10 1.9 6.6 0.8 2.1z"/></svg>
          <span>404 555 0172</span>
        </li>
        <li class="contact__item">
          <svg class="contact__icon contact__icon--stroke" viewBox="0 0 12 12" aria-hidden="true"><circle cx="6" cy="6" r="2"/><path d="M8 4v2.6c0 1.2 2.2 1.2 2.2-0.6A4.5 4.5 0 1 0 8 9.8"/></svg>
          <span>mferrand@krtecnica.com</span>
        </li>
        <li class="contact__item">
          <svg class="contact__icon contact__icon--stroke" viewBox="0 0 12 12" aria-hidden="true"><circle cx="6" cy="6" r="4.8"/><ellipse cx="6" cy="6" rx="2" ry="4.8"/><path d="M1.2 6h9.6M2 3.5h8M2 8.5h8"/></svg>
          <span>www.krtecnica.com</span>
        </li>
        <li class="contact__item">
          <svg class="contact__icon" viewBox="0 0 12 14" style="height:15px" aria-hidden="true"><path d="M6 0a4.6 4.6 0 0 0-4.6 4.6C1.4 8 6 14 6 14s4.6-6 4.6-9.4A4.6 4.6 0 0 0 6 0zm0 6.4a1.8 1.8 0 1 1 0-3.6 1.8 1.8 0 0 1 0 3.6z"/></svg>
          <span>418 Volta drive, Suite 200<br>Brookfield,GA 30090</span>
        </li>
      </ul>
    </div>
  </section>
  <section class="card card--back">
    <div class="wordmark"><span class="wordmark__square"></span>KR Tecnica</div>
  </section>
</main>
</body>
</html>
```